Home Inspection Postcard Design

Home inspection. Attached is my old postcard. I would like the card to have the same verbage on it - front and back. but I would like the house graphic and the colors to be blues. The only changes to the information is the website address is www.brightoakhps.com. THe PO Box is now 381 rather than 647, and I wanted to add my email address which is brightoakhps@quillmail.net. I would like to keep the $25 off box but add "or a 10% military discount, which ever is greater" or something like that .If you could mock something up for me I would really appreciate it. I would also like a glossy finish on the cards

Home Inspection

```html
<!DOCTYPE html>
<html lang="en">
<head>
<meta charset="utf-8">
<title>Bright Oak Home Inspection Postcard</title>
<link rel="stylesheet" href="https://fonts.googleapis.com/css2?family=Open+Sans:ital,wght@0,400;0,600;0,700;1,800&family=Lato:wght@700;900&family=Great+Vibes&display=swap">
<style>
:root{
  --red:#e03a25;
  --red-dark:#c42a1a;
  --navy:#1c3d7a;
  --navy-dark:#12295a;
  --blue:#2358b8;
  --ink:#2b2b2b;
  --grey-box:#dcdcdc;
  --page:#efefef;
  --white:#ffffff;
}
*{box-sizing:border-box;margin:0;padding:0}
html,body{width:907px;height:1200px;overflow:hidden;background:var(--page)}
body{position:relative;font-family:"Open Sans",Arial,sans-serif;color:var(--ink)}
.card{position:absolute;left:117px;width:686px;height:531px;background:var(--white);overflow:hidden;box-shadow:0 2px 6px rgba(0,0,0,.25)}
.card--front{top:35px}
.card--back{top:630px}
.abs{position:absolute}

/* front */
.header-band{left:0;top:0;width:686px;height:100px;background:linear-gradient(90deg,var(--red-dark),var(--red) 60%,#e8472f)}
.headline{right:20px;top:28px;font-style:italic;font-weight:800;font-size:35px;color:var(--white);letter-spacing:-.3px;white-space:nowrap}
.tagline{right:22px;top:68px;font-family:"Great Vibes",cursive;font-size:17px;color:var(--white)}
.photo-front{left:0;top:62px;width:430px;height:420px;background:linear-gradient(180deg,#c9d9ec 0%,#aab7c4 35%,#8e8d86 55%,#5d8f3a 75%,#4c7f2c 100%);
  -webkit-mask-image:linear-gradient(90deg,#000 75%,transparent 100%);mask-image:linear-gradient(90deg,#000 75%,transparent 100%)}
.text-col{left:397px;top:103px;width:282px}
.section-title{font-weight:700;font-size:18.5px;color:var(--navy);line-height:1.1}
.body-copy{font-size:10.6px;line-height:13.6px;margin-top:8px}
.body-copy + .body-copy{margin-top:6px}
.offer-box{left:397px;top:312px;width:275px;height:48px;background:var(--grey-box);border:1px dashed var(--red);display:flex;align-items:center;padding-left:6px}
.offer-amount{font-weight:700;font-size:37px;color:var(--blue);line-height:1}
.offer-note{margin-left:6px;font-weight:600;font-size:12.5px;line-height:15px;color:var(--ink)}
.military{left:400px;top:368px;font-size:12.2px}
.military b{color:var(--blue)}
.wave{left:0;bottom:0;width:686px}
.brand-circle{left:31px;top:378px;width:120px;height:120px;border-radius:50%;background:var(--white);border:3px solid #e6e6e6;box-shadow:0 1px 4px rgba(0,0,0,.3);display:flex;align-items:center;justify-content:center;text-align:center}
.brand-name{font-weight:700;font-size:15px;line-height:17px;color:var(--navy)}
.contact{font-weight:600;font-size:11px;color:var(--white);white-space:nowrap;display:flex;align-items:center;gap:6px}
.contact svg{flex:none}

/* back */
.photo-back-faint{left:0;top:0;width:230px;height:140px;background:linear-gradient(135deg,#e4e6ea,#f7f7f7 70%,#fff)}
.photo-back{left:350px;top:0;width:336px;height:430px;background:linear-gradient(180deg,#eef1f3 0%,#d7d3c8 40%,#b9b2a3 60%,#5f8e34 82%,#4f8a2c 100%);
  -webkit-mask-image:linear-gradient(90deg,transparent 0%,#000 25%);mask-image:linear-gradient(90deg,transparent 0%,#000 25%)}
.call-label{left:18px;top:66px;font-family:"Lato",sans-serif;font-weight:900;font-size:16px;color:var(--red)}
.call-phone{left:18px;top:84px;font-family:"Lato",sans-serif;font-weight:900;font-size:22.5px;color:var(--navy)}
.brand-back{left:182px;top:78px;width:150px;text-align:center}
.ribbon{left:0;top:160px;width:355px;height:34px;background:linear-gradient(90deg,var(--red-dark),var(--red));color:var(--white);font-weight:600;font-size:17.5px;line-height:34px;padding-left:18px}
.ribbon-tip{left:320px;top:148px}
.back-copy{left:18px;top:204px;width:340px;font-size:10.8px;line-height:15.1px;text-align:justify}
</style>
</head>
<body>

<section class="card card--front">
  <div class="abs photo-front" role="img" aria-label="Photo of a large two-storey grey house with lit windows, paved driveway and green lawn at dusk"></div>
  <div class="abs header-band"></div>
  <h1 class="abs headline">We Leave No Stone Unturned</h1>
  <p class="abs tagline">Licensed, Certified &amp; Insured</p>

  <div class="abs text-col">
    <h2 class="section-title">Confidence In Home BUYING</h2>
    <p class="body-copy">Enjoy the comfort of peace-of-mind before buying your new home. Our trained professionals inspect the property and imediately present you with a detailed, yet clear report. They will answer any questions you may have.</p>
    <p class="body-copy">Join our expenenced inspectors in their tour of the property. They will acquaint you with its strenghts and weekness. You will feel confident in their judgement and throughness. Many Realtors, Sellers, Home Buyers, Mortgage companies and relocation companies have used our comprehensive report and services to their satisfaction.</p>
  </div>

  <div class="abs offer-box">
    <span class="offer-amount">$25 Off</span>
    <span class="offer-note">Services<br>with this postcard</span>
  </div>
  <p class="abs military">or a <b>10%</b> military discount, which ever is greater</p>

  <svg class="abs wave" viewBox="0 0 686 140" height="140" aria-hidden="true">
    <path d="M0 62 C150 20 300 10 450 30 C560 45 630 40 686 20 L686 140 L0 140Z" fill="var(--red)"/>
    <path d="M0 70 C150 30 300 20 450 40 C560 55 630 50 686 30 L686 140 L0 140Z" fill="var(--white)"/>
    <path d="M0 80 C150 42 300 32 450 52 C560 67 630 62 686 42 L686 140 L0 140Z" fill="var(--navy)"/>
  </svg>

  <div class="abs brand-circle"><span class="brand-name">Bright Oak<br>Home Inspection</span></div>

  <div class="abs contact" style="left:325px;top:477px">912-555-0143
    <svg width="9" height="9" viewBox="0 0 10 10"><path d="M2 0l2 2.5-1.2 1.4a6 6 0 0 0 3.3 3.3L7.5 6 10 8 8.6 10C4 10 0 6 0 1.4Z" fill="var(--red)"/></svg></div>
  <div class="abs contact" style="left:258px;top:497px">brightoakhps@quillmail.net
    <svg width="10" height="7" viewBox="0 0 10 7"><rect width="10" height="7" rx="1" fill="var(--red)"/></svg></div>
  <div class="abs contact" style="right:26px;top:465px;justify-content:flex-end">Bright Oak Home Inspection Services
    <svg width="8" height="10" viewBox="0 0 8 10"><path d="M4 0a4 4 0 0 1 4 4c0 3-4 6-4 6S0 7 0 4a4 4 0 0 1 4-4Z" fill="var(--red)"/><circle cx="4" cy="4" r="1.5" fill="var(--navy)"/></svg></div>
  <div class="abs contact" style="right:40px;top:479px">P.O. Box 381, Harlow, GA 31399</div>
  <div class="abs contact" style="right:26px;top:497px">www.brightoakhps.com
    <svg width="8" height="8" viewBox="0 0 8 8"><circle cx="4" cy="4" r="4" fill="var(--red)"/></svg></div>
</section>

<section class="card card--back">
  <div class="abs photo-back-faint" role="img" aria-label="Faded photo of a house facade"></div>
  <div class="abs photo-back" role="img" aria-label="Photo of a white house porch with columns, shuttered windows, patio chairs, hedge and lawn"></div>

  <p class="abs call-label">CALL US TODAY AT</p>
  <p class="abs call-phone">912-555-0143</p>
  <div class="abs brand-back"><span class="brand-name">Bright Oak<br>Home Inspection Services LLC</span></div>

  <svg class="abs ribbon-tip" width="36" height="14" viewBox="0 0 36 14" aria-hidden="true"><path d="M0 14V0l36 12v2Z" fill="var(--red-dark)"/></svg>
  <h2 class="abs ribbon">Why Do I Need An Inspection?</h2>

  <p class="abs back-copy">The purchase of home or comercial building is one of the largest single investments you will ever make. You should know what to expect - in terms of needed and possible repairs and maintenance. A fresh coat of paint could be hiding serious problems. Stains on the ceiling may indicate a chronic roof leak or may be simply the result of a sinle incident. The inspector reviews these and other clues, then presents a professional opinion as to the condision of the property to help you avoid unpleasant surprises afterward. Ofcourse, an inspection may also point out the positive aspects of a building, as well as the type of maintenance needed to keep it in proper shape. After the inspection, you will have a much clearer understanding of the property, and be able to make you purchasing decision confidently.</p>

  <svg class="abs wave" viewBox="0 0 686 140" height="140" aria-hidden="true">
    <path d="M0 40 C120 0 260 10 400 35 C520 55 610 60 686 50 L686 140 L0 140Z" fill="var(--red)"/>
    <path d="M0 50 C120 12 260 22 400 47 C520 67 610 72 686 62 L686 140 L0 140Z" fill="var(--white)"/>
    <path d="M0 60 C120 24 260 34 400 59 C520 79 610 84 686 74 L686 140 L0 140Z" fill="var(--navy)"/>
  </svg>

  <div class="abs contact" style="left:18px;top:472px">
    <svg width="8" height="10" viewBox="0 0 8 10"><path d="M4 0a4 4 0 0 1 4 4c0 3-4 6-4 6S0 7 0 4a4 4 0 0 1 4-4Z" fill="var(--red)"/><circle cx="4" cy="4" r="1.5" fill="var(--navy)"/></svg>Bright Oak Home Inspection Services</div>
  <div class="abs contact" style="left:32px;top:486px">P.O. Box 381, Harlow, GA 31399</div>
  <div class="abs contact" style="left:18px;top:504px">
    <svg width="8" height="8" viewBox="0 0 8 8"><circle cx="4" cy="4" r="4" fill="var(--red)"/></svg>www.brightoakhps.com</div>
  <div class="abs contact" style="left:252px;top:504px">
    <svg width="10" height="7" viewBox="0 0 10 7"><rect width="10" height="7" rx="1" fill="var(--red)"/></svg>brightoakhps@quillmail.net</div>
</section>

</body>
</html>
```